" Window Blinds and Shutters Business Card Design"

We require a business card design for a new windows blinds and shutters company based in Sydney.
The business name is 'Larkvale Blinds and Shutters'.
We supply and install homes and businesses with internal and external window furnishings and finishes. This includes varieties of window blinds and window shutters.

Benefits of Larkvale Blinds and Shutters :
Added security and privacy,
The ability to control the amount of sunlight,
Regulate internal temperature.

Blinds varieties:
Roller Blinds, Double Roller Blinds, Roman Blinds, Vertical Blinds, Aluminium venetians, Timber venetians and PVC Venetians.

Shutters varieties:
Plantation Shutters, Aluminium Louvre Shutters, Roller Shutters and Security Shutters .
Updates

Hi Designers,

Please have a look at my Business card design brief. I need your help to start my new business.

Thanks,

Dorian.

Reason: not 100% happy with the options available, close to 90% happy, need a little more refinement. Thank You & Good Luck

Target Market(s)

Home owners, business owners, shift workers , and new home builders.

Industry/Entity Type

Security

Contact Information for Business Card

Larkvale Blinds and Shutters,

Dorian Kettlewell mobile: 0487561904,
Priya Hensworth mobile: 0472846015,

email: dorian.kettlewell@mailgrove.net
web: larkvaleblindsandshutters.com.au

Colors
ffffff
9d9d9d
f78f20

Requirements
Must have
• ON FRONT OF CARD
I have attached a picture of logo and need a designer to design a font logo for Larkvale Blinds and Shutters similar, or open to suggestions.

FRONT OF CARD
Company message/:
"Safeguarding windows by design"

BACK OF CARD
'For a FREE measure & quote call Dorian - 0487561904"
Nice to have
• Elegant yet professional.

Soft colours appealing to both male & female clients.

Should not have

• Unprofessional fonts

```html
<!DOCTYPE html>
<html lang="en">
<head>
<meta charset="utf-8">
<title>Larkvale Blinds and Shutters — Business Card</title>
<link rel="stylesheet" href="https://fonts.googleapis.com/css2?family=Open+Sans:wght@400;600;700;800&family=Michroma&display=swap">
<style>
  :root {
    --stage: #d3d3d3;
    --white: #ffffff;
    --orange: #f78f20;
    --orange-deep: #e8781a;
    --charcoal: #4a4a4c;
    --charcoal-dark: #38383a;
    --grey-mid: #9d9d9d;
    --ink: #2b2b2b;
  }
  * { box-sizing: border-box; margin: 0; padding: 0; }
  html, body { width: 1200px; height: 900px; overflow: hidden; }
  body {
    background: var(--stage);
    font-family: "Open Sans", Arial, sans-serif;
    display: flex;
    align-items: center;
    justify-content: center;
    gap: 40px;
  }
  .card {
    width: 540px;
    height: 315px;
    border-radius: 22px;
    overflow: hidden;
    position: relative;
  }
  .surface-dark {
    background: linear-gradient(160deg, var(--charcoal) 0%, var(--charcoal-dark) 100%);
  }

  /* Front */
  .card-front { display: flex; flex-direction: column; background: var(--white); }
  .brand {
    height: 140px;
    display: flex;
    flex-direction: column;
    align-items: center;
    justify-content: center;
    color: var(--orange);
    font-weight: 800;
    text-transform: uppercase;
    line-height: 1;
  }
  .brand-name { font-size: 62px; letter-spacing: 2px; }
  .brand-sub { font-size: 19px; letter-spacing: 7px; margin-top: 8px; }
  .tagline-band {
    height: 16px;
    background: linear-gradient(90deg, var(--orange) 0%, var(--orange-deep) 100%);
    display: flex;
    align-items: center;
    justify-content: center;
  }
  .tagline {
    font-family: "Michroma", "Arial", sans-serif;
    font-size: 9.5px;
    letter-spacing: 8px;
    color: var(--ink);
    text-transform: uppercase;
  }
  .contacts { flex: 1; padding: 10px 24px; color: var(--white); font-size: 15px; line-height: 1.28; }
  .contact-name { color: var(--orange); font-weight: 600; }
  .contact-line { display: flex; align-items: center; gap: 6px; }
  .contact-line svg { width: 13px; height: 13px; flex: none; }
  .contact-online { margin-top: 10px; }

  /* Back */
  .card-back {
    display: flex;
    flex-direction: column;
    align-items: center;
    justify-content: center;
    text-align: center;
    color: var(--white);
  }
  .range-title {
    font-family: "Michroma", "Arial", sans-serif;
    color: var(--orange);
    font-size: 11px;
    text-transform: uppercase;
    margin-bottom: 3px;
  }
  .range-list { list-style: none; margin-bottom: 18px; }
  .range-list li {
    font-family: "Michroma", "Arial", sans-serif;
    font-size: 9.5px;
    letter-spacing: 1.5px;
    text-transform: uppercase;
    line-height: 1.5;
  }
  .offer { color: var(--orange); font-size: 16px; font-weight: 600; line-height: 1.25; margin-top: 6px; }
</style>
</head>
<body>

<svg width="0" height="0" style="position:absolute" aria-hidden="true">
  <symbol id="icon-phone" viewBox="0 0 24 24">
    <path fill="#f78f20" d="M6.6 10.8a15.1 15.1 0 0 0 6.6 6.6l2.2-2.2a1 1 0 0 1 1-.25 11.4 11.4 0 0 0 3.6.6 1 1 0 0 1 1 1V20a1 1 0 0 1-1 1A17 17 0 0 1 3 4a1 1 0 0 1 1-1h3.5a1 1 0 0 1 1 1c0 1.25.2 2.45.6 3.6a1 1 0 0 1-.25 1z"/>
  </symbol>
  <symbol id="icon-mail" viewBox="0 0 24 24">
    <circle cx="12" cy="12" r="12" fill="#f78f20"/>
    <rect x="5.5" y="7.5" width="13" height="9" rx="1" fill="#ffffff"/>
    <path d="M5.5 8l6.5 5 6.5-5" fill="none" stroke="#f78f20" stroke-width="1.4"/>
  </symbol>
  <symbol id="icon-globe" viewBox="0 0 24 24">
    <circle cx="12" cy="12" r="11" fill="#f78f20"/>
    <g fill="none" stroke="#ffffff" stroke-width="1.3">
      <circle cx="12" cy="12" r="7.5"/>
      <ellipse cx="12" cy="12" rx="3.3" ry="7.5"/>
      <path d="M4.5 12h15M6 8h12M6 16h12"/>
    </g>
  </symbol>
</svg>

<section class="card card-front" aria-label="Card front">
  <header class="brand">
    <span class="brand-name">Larkvale</span>
    <span class="brand-sub">Blinds and Shutters</span>
  </header>
  <div class="tagline-band"><p class="tagline">Safeguarding windows by design</p></div>
  <div class="contacts surface-dark">
    <p class="contact-name">Dorian Kettlewell</p>
    <p class="contact-line"><svg><use href="#icon-phone"/></svg>0487561904</p>
    <p class="contact-name">Priya Hensworth</p>
    <p class="contact-line"><svg><use href="#icon-phone"/></svg>0472846015</p>
    <div class="contact-online">
      <p class="contact-line"><svg><use href="#icon-mail"/></svg>dorian.kettlewell@mailgrove.net</p>
      <p class="contact-line"><svg><use href="#icon-globe"/></svg>larkvaleblindsandshutters.com.au</p>
    </div>
  </div>
</section>

<section class="card card-back surface-dark" aria-label="Card back">
  <h2 class="range-title">Blinds Varieties</h2>
  <ul class="range-list">
    <li>Roller Blinds</li>
    <li>Double Roller Blinds</li>
    <li>Roman Blinds</li>
    <li>Vertical Blinds</li>
    <li>Aluminium Venetians</li>
    <li>Timber Venetians and PVC Venetians</li>
  </ul>
  <h2 class="range-title">Shutters Varieties</h2>
  <ul class="range-list">
    <li>Plantation Shutters</li>
    <li>Aluminium Louvre Shutters</li>
    <li>Roller Shutters and Security Shutters</li>
  </ul>
  <p class="offer">For a FREE measure &amp; quote<br>call Dorian - 0487561904</p>
</section>

</body>
</html>
```